Business Card Design - Crisp & Clean

Looking for a new clean and crisp business card design. Design must incorporate our corporate colors (see attached style sheet). We're a pretty fun loving group who likes to keep it light while still portraying a professional image. Card should incorporate both our logo and our mascot (see attachment). Card should be double sided and should have room for our social media - Gleamrow, Brisk Hub and Zumbly on the back. Font selections do not have to match the style guide.

```html
<!DOCTYPE html>
<html lang="en">
<head>
<meta charset="utf-8">
<title>BrightPeople Business Cards</title>
<link rel="stylesheet" href="https://fonts.googleapis.com/css2?family=Exo+2:wght@400;600;800&display=swap">
<style>
  :root {
    --yellow: #f6b51e;
    --blue: #4f7cc6;
    --orange: #f25a22;
    --ink: #1d1d1b;
    --grey: #5a5a5a;
    --paper: #ffffff;
    --stage: #e9e4da;
  }
  * { box-sizing: border-box; margin: 0; padding: 0; }
  html, body { width: 1200px; height: 675px; overflow: hidden; }
  body {
    background: var(--stage);
    font-family: "Exo 2", sans-serif;
    position: relative;
  }
  .card {
    position: absolute;
    top: 188px;
    width: 520px;
    height: 300px;
    background: var(--paper);
    overflow: hidden;
    box-shadow: 0 6px 18px rgba(0,0,0,.18);
  }
  .card-back { left: 50px; }
  .card-front { left: 630px; }
  .card svg.frame { position: absolute; inset: 0; }

  .brand { position: absolute; display: flex; align-items: center; gap: 8px; white-space: nowrap; }
  .brand-dot { width: 22px; height: 22px; border-radius: 50%; background: var(--yellow); flex: none; }
  .brand-name { font-weight: 800; font-size: 26px; color: var(--ink); letter-spacing: .5px; }
  .brand-tagline {
    position: absolute; font-size: 6.5px; font-weight: 600; white-space: nowrap;
    color: var(--ink); letter-spacing: .4px; text-transform: uppercase;
  }

  .mascot {
    position: absolute;
    background: linear-gradient(180deg, #f2f2f2 0%, #d9d3c8 60%, #6b4a34 100%);
    border-radius: 10px;
  }

  /* back */
  .card-back .brand { left: 22px; top: 104px; gap: 6px; }
  .card-back .brand-dot { width: 18px; height: 18px; }
  .card-back .brand-name { font-size: 20px; letter-spacing: .2px; }
  .card-back .brand-tagline { left: 46px; top: 130px; font-size: 5.5px; letter-spacing: .2px; }
  .card-back .mascot { left: 208px; top: 72px; width: 112px; height: 160px; }
  .socials { position: absolute; left: 340px; top: 98px; width: 145px; }
  .social { text-align: center; margin-bottom: 14px; }
  .social-network { font-size: 15px; font-weight: 800; }
  .social-handle { font-size: 10px; color: var(--grey); padding-bottom: 3px; }
  .social-rule { height: 2px; }
  .social.briskhub .social-network { color: var(--yellow); }
  .social.briskhub .social-rule { background: var(--yellow); }
  .social.zumbly .social-network { color: var(--orange); }
  .social.zumbly .social-rule { background: var(--orange); }
  .social.gleamrow .social-network { color: var(--blue); }
  .social.gleamrow .social-rule { background: var(--blue); }

  /* front */
  .card-front .brand { left: 40px; top: 36px; }
  .card-front .brand-tagline { left: 70px; top: 68px; }
  .name-bar {
    position: absolute; left: 0; top: 112px; height: 26px;
    display: flex;
  }
  .name-bar .tab { width: 34px; background: var(--yellow); }
  .name-bar .name {
    background: var(--orange); color: #fff; font-size: 15px;
    padding: 3px 16px 0 10px; font-weight: 400; letter-spacing: .3px;
  }
  .role { position: absolute; left: 44px; top: 142px; font-size: 10px; color: var(--yellow); font-weight: 600; }
  .address { position: absolute; left: 30px; top: 166px; font-size: 13px; color: var(--grey); line-height: 15px; font-style: normal; }
  .hero-panel {
    position: absolute; left: 352px; top: 58px; width: 168px; height: 174px;
    background: var(--yellow); border-radius: 12px 0 0 12px;
  }
  .card-front .mascot { left: 378px; top: 80px; width: 118px; height: 138px; }
  .contact {
    position: absolute; left: 272px; top: 246px; color: #fff; font-size: 13px;
    list-style: none; line-height: 24px;
  }
  .contact li { display: flex; align-items: center; gap: 8px; }
  .contact svg { width: 14px; height: 14px; }
</style>
</head>
<body>

<section class="card card-back">
  <svg class="frame" viewBox="0 0 520 300" width="520" height="300">
    <rect x="0" y="0" width="68" height="12" fill="var(--yellow)"/>
    <polygon points="74,0 520,0 520,20 88,20" fill="var(--blue)"/>
    <polygon points="0,280 268,280 282,300 0,300" fill="var(--blue)"/>
    <polygon points="276,280 520,280 520,300 290,300" fill="var(--yellow)"/>
  </svg>
  <div class="brand"><span class="brand-dot"></span><span class="brand-name">BrightPeople</span></div>
  <div class="brand-tagline">HR Process Management Solutions</div>
  <div class="mascot" role="img" aria-label="Company mascot, a white-haired professor, pointing toward the social links"></div>
  <div class="socials">
    <div class="social briskhub">
      <div class="social-network">Brisk Hub</div>
      <div class="social-handle">BrightPeople</div>
      <div class="social-rule"></div>
    </div>
    <div class="social zumbly">
      <div class="social-network">Zumbly</div>
      <div class="social-handle">@BrightPeople</div>
      <div class="social-rule"></div>
    </div>
    <div class="social gleamrow">
      <div class="social-network">Gleamrow</div>
      <div class="social-handle">BrightPeople</div>
      <div class="social-rule"></div>
    </div>
  </div>
</section>

<section class="card card-front">
  <div class="brand"><span class="brand-dot"></span><span class="brand-name">BrightPeople</span></div>
  <div class="brand-tagline">HR Process Management Solutions</div>
  <div class="name-bar"><span class="tab"></span><span class="name">Dana Whitfield</span></div>
  <div class="role">Managing Director</div>
  <address class="address">482 North Elm Avenue<br>Marlow, TX 75021<br>United States</address>
  <div class="hero-panel"></div>
  <div class="mascot" role="img" aria-label="Company mascot, a white-haired professor, carrying a large light bulb"></div>
  <svg class="frame" viewBox="0 0 520 300" width="520" height="300">
    <polygon points="258,232 520,232 520,300 240,300 240,250" fill="var(--blue)"/>
  </svg>
  <ul class="contact">
    <li>
      <svg viewBox="0 0 24 24"><path d="M6.6 10.8a15 15 0 0 0 6.6 6.6l2.2-2.2a1 1 0 0 1 1-.25 11.4 11.4 0 0 0 3.6.57 1 1 0 0 1 1 1V20a1 1 0 0 1-1 1A17 17 0 0 1 3 4a1 1 0 0 1 1-1h3.5a1 1 0 0 1 1 1c0 1.25.2 2.45.57 3.57a1 1 0 0 1-.25 1z" fill="#fff"/></svg>
      <span>1-800-555-0142</span>
    </li>
    <li>
      <svg viewBox="0 0 24 24"><rect x="2" y="5" width="20" height="14" rx="1" fill="none" stroke="#fff" stroke-width="2"/><path d="M3 6l9 7 9-7" fill="none" stroke="#fff" stroke-width="2"/></svg>
      <span>team@brightpeople.com</span>
    </li>
  </ul>
</section>

</body>
</html>
```